Real Estate Agent Business Card Needs a New Eye Catching Design

Looking for a designer that can revamp a current business card.
Looking for something with a lot more style.
Something that will catch the eye

Included in the file:
The old business card. (Old Business Card)
A new place holder image to be used as headshot. (Temp Headshot)
Homevane KT Logo (KT logo)
Fair Dwelling Access Logo (AC logo)

The working PSD file will need to be delivered with the individual layers separated and edible. (I'll being changing the new headshot later)
Any fonts used also need to be delivered.

Overall, the old business card has the elements but in a horrible state.
If you have any questions, please feel free to reach out.

Thank you

Glen

Target Market(s)

Individuals want to either sale or buy a home

Industry/Entity Type

Real Estate Agent

Design Requirements:
Headshot needs to be a head and shoulders and have a transparent background.

The American Flag should implemented into the design somehow.

Both the KT logo and AC logo need to be incorporated.

All information on the OLD Business Card should be included.

Requirements
Must have
• Transparent head shot set against the final background
• American Flag and/or colors-theme incorporated
• KT logo and AC logo incorporated

```html
<!DOCTYPE html>
<html lang="en">
<head>
<meta charset="utf-8">
<title>Jessa Morland – Business Card</title>
<link rel="stylesheet" href="https://fonts.googleapis.com/css2?family=Roboto:wght@400;500;700&display=swap">
<style>
  :root {
    --backdrop: #e9e9ec;
    --card: #ffffff;
    --gold-light: #ecc06a;
    --gold-mid: #dca850;
    --gold-dark: #c8923a;
    --sweater-navy: #2b2a3a;
    --accent-blue: #2f8fd6;
    --flag-red: #c8283a;
    --flag-navy: #1f2f5c;
    --text-dark: #3a3a3a;
    --text-muted: #7a7a7a;
    --logo-grey: #4a4a4a;
  }
  * { box-sizing: border-box; margin: 0; padding: 0; }
  html, body {
    width: 1200px; height: 900px; overflow: hidden;
    background: var(--backdrop);
    font-family: "Roboto", Arial, sans-serif;
  }
  .canvas {
    width: 1200px; height: 900px;
    display: flex; align-items: center; justify-content: center;
  }
  .business-card {
    width: 1050px; height: 600px;
    background: var(--card);
    display: flex;
    box-shadow: 0 10px 30px rgba(0,0,0,0.12);
    overflow: hidden;
  }
  .headshot-area {
    width: 440px; height: 100%;
    background:
      radial-gradient(ellipse 62% 48% at 50% 100%, var(--sweater-navy) 0%, rgba(43,42,58,0.85) 55%, rgba(43,42,58,0) 100%),
      radial-gradient(circle at 48% 34%, rgba(236,200,160,0.55) 0%, rgba(236,200,160,0) 22%),
      linear-gradient(160deg, var(--gold-light), var(--gold-mid) 55%, var(--gold-dark));
  }
  .flag-band {
    width: 22px; height: 100%;
    display: flex; flex-direction: column;
  }
  .flag-band .band-navy { height: 34%; background: var(--flag-navy); }
  .flag-band .stripes {
    flex: 1;
    background: repeating-linear-gradient(180deg, var(--flag-red) 0 30px, var(--card) 30px 60px);
  }
  .info-panel {
    flex: 1;
    position: relative;
    padding: 48px 60px 40px 40px;
    text-align: right;
    color: var(--text-dark);
  }
  .logo-row {
    display: flex; justify-content: flex-end; align-items: center; gap: 28px;
    margin-bottom: 30px;
  }
  .logo-mark {
    display: flex; align-items: center; gap: 10px;
    font-size: 20px; font-weight: 500; color: var(--logo-grey);
  }
  .logo-mark .mark-square { width: 30px; height: 30px; background: var(--logo-grey); }
  .agent-name {
    font-size: 50px; font-weight: 700; color: var(--accent-blue);
    letter-spacing: 1px; line-height: 1.1;
  }
  .agent-title { font-size: 22px; color: var(--text-muted); margin-top: 4px; }
  .accent-rule {
    width: 150px; height: 3px;
    background: linear-gradient(90deg, var(--flag-red) 0 33%, var(--card) 33% 40%, var(--accent-blue) 40%);
    margin: 16px 0 18px auto;
  }
  .address { font-size: 22px; font-weight: 500; line-height: 1.4; }
  .contact-list {
    list-style: none; margin-top: 26px;
    font-size: 22px; font-weight: 500; line-height: 1.55;
  }
  .contact-list li { display: flex; justify-content: flex-end; align-items: center; gap: 12px; }
  .contact-list svg { width: 18px; height: 18px; fill: var(--accent-blue); }
  .email-footer {
    position: absolute; left: 40px; bottom: 40px;
    font-size: 20px; font-weight: 500; color: var(--text-dark);
  }
</style>
</head>
<body>
<div class="canvas">
  <article class="business-card">
    <div class="headshot-area" role="img" aria-label="Head-and-shoulders portrait of the agent with transparent background, set on warm gold"></div>
    <div class="flag-band" aria-hidden="true"><div class="band-navy"></div><div class="stripes"></div></div>
    <section class="info-panel">
      <div class="logo-row">
        <div class="logo-mark"><span class="mark-square"></span>Homevane KT</div>
        <div class="logo-mark"><span class="mark-square"></span>Fair Dwelling Access</div>
      </div>
      <h1 class="agent-name">JESSA MORLAND</h1>
      <p class="agent-title">Homevane</p>
      <div class="accent-rule"></div>
      <p class="address">2210 W. Route 95, Dunmore<br>NV 89120</p>
      <ul class="contact-list">
        <li>555-014-2231
          <svg viewBox="0 0 18 18"><rect x="4" y="0" width="10" height="18" rx="2"/><rect x="6" y="2" width="6" height="11" fill="#fff"/></svg>
        </li>
        <li>555-016-7742
          <svg viewBox="0 0 18 18"><path d="M4 1l3 4-2 2c1 2 4 5 6 6l2-2 4 3-2 3C8 17 1 10 1 3z"/></svg>
        </li>
        <li>555-016-7790
          <svg viewBox="0 0 18 18"><rect x="4" y="1" width="10" height="5"/><rect x="1" y="6" width="16" height="8" rx="1"/><rect x="4" y="11" width="10" height="6" fill="#fff" stroke="#2f8fd6" stroke-width="1.5"/></svg>
        </li>
        <li>jmorland.homesales@mailbox.com
          <svg viewBox="0 0 18 18"><rect x="1" y="3" width="16" height="12" rx="1"/><path d="M1 4l8 6 8-6" fill="none" stroke="#fff" stroke-width="1.5"/></svg>
        </li>
      </ul>
      <p class="email-footer">jmorland.homesales@mailbox.com</p>
    </section>
  </article>
</div>
</body>
</html>
```